Velbrook Naturals - High Quality Organic Cleaning Product

A product label for a foaming hand soap. Company is called "Velbrook Naturals" and the tagline is "Pure Plant Fresh". Maybe lighter blue background with red letters, but open to what looks good. Want it to be a simple, clean and sophisticated design that looks fresh and stands out. This product has high quality organic ingredients hence the ingredients are "velbrook naturals" than other toxic chemical cleaners. Attached is label specifications as well as an image for stock language for left and right side of label for reference. Parts can be omitted, added or mixed and matched as needed.
Went on vacation/holiday
Moms

```html
<!DOCTYPE html>
<html lang="en">
<head>
<meta charset="utf-8">
<title>Velbrook Naturals – Foaming Hand Soap Label</title>
<link rel="stylesheet" href="https://fonts.googleapis.com/css2?family=Arimo:wght@400;700&display=swap">
<style>
  :root {
    --leaf-green: #3fe51f;
    --aloe-light: #9fd88a;
    --aloe-dark: #3e8a3a;
    --ink: #111111;
    --paper: #ffffff;
  }
  * { margin: 0; padding: 0; box-sizing: border-box; }
  html, body { width: 1200px; height: 488px; overflow: hidden; background: var(--paper); }
  body { font-family: "Arimo", Arial, sans-serif; color: var(--ink); }

  .label { position: relative; width: 1200px; height: 488px; overflow: hidden; background: var(--paper); }
  .label-shapes { position: absolute; inset: 0; }

  .fine-print { position: absolute; font-size: 9.5px; line-height: 14px; }
  .fine-print--left-top { left: 10px; top: 8px; width: 150px; color: var(--paper); }
  .fine-print--right-top { left: 966px; top: 10px; width: 200px; color: var(--paper); }
  .fine-print--ingredients { left: 10px; top: 420px; width: 292px; font-size: 8px; line-height: 11px; }

  .info-box {
    position: absolute; left: 6px; top: 162px; width: 296px; height: 246px;
    border: 3px solid var(--ink); border-radius: 16px;
    padding: 14px 16px; font-size: 12.5px; line-height: 16px;
  }

  .product-art {
    position: absolute; left: 510px; top: 62px; width: 150px; height: 150px;
    border-radius: 50% 50% 40% 40%;
    background: radial-gradient(circle at 50% 60%, var(--aloe-light), var(--aloe-dark));
  }

  .brand { position: absolute; left: 330px; top: 220px; width: 520px; text-align: center; font-weight: 700; }
  .brand-name { font-size: 46px; line-height: 48px; }
  .brand-name--second { font-size: 36px; line-height: 42px; }
  .tagline { position: absolute; left: 330px; top: 316px; width: 520px; text-align: center; font-size: 20px; line-height: 24px; }

  .direction { position: absolute; left: 855px; top: 298px; width: 305px; text-align: center; }
  .direction-title { font-size: 23px; font-weight: 700; text-align: left; padding-left: 10px; margin-bottom: 6px; }
  .direction-body { font-size: 13px; line-height: 16px; }
</style>
</head>
<body>
<main class="label">
  <svg class="label-shapes" width="1200" height="488" viewBox="0 0 1200 488" aria-hidden="true">
    <defs>
      <clipPath id="panel-clip">
        <path d="M590 48 C650 80 760 130 820 200 C845 230 850 260 850 300 V425 Q850 450 825 450 H355 Q330 450 330 425 V300 C330 260 335 230 360 200 C420 130 530 80 590 48 Z"/>
      </clipPath>
    </defs>
    <path fill="var(--leaf-green)" d="M0 0 H318 C300 90 180 175 0 190 Z"/>
    <path fill="var(--leaf-green)" d="M840 0 H1200 V205 C1100 215 960 200 880 120 C855 90 845 40 840 0 Z"/>
    <path fill="var(--leaf-green)" d="M1200 300 C1170 340 1158 420 1165 488 H1200 Z"/>
    <g clip-path="url(#panel-clip)">
      <path fill="var(--leaf-green)" d="M320 380 C450 350 560 385 700 362 C780 350 830 352 860 356 V460 H320 Z"/>
    </g>
    <path fill="none" stroke="var(--ink)" stroke-width="5" d="M590 48 C650 80 760 130 820 200 C845 230 850 260 850 300 V425 Q850 450 825 450 H355 Q330 450 330 425 V300 C330 260 335 230 360 200 C420 130 530 80 590 48 Z"/>
  </svg>

  <p class="fine-print fine-print--left-top">Pure plant foam for gentle hands. Made with aloe and mild oils, free of harsh dyes. Rinse clean, leaves skin soft and fresh every day.</p>

  <div class="info-box">
    Lorem ipsum dolor sit amet, consectetur adipiscing elit, sed do eiusmod tempor incididunt ut labore et dolore magna aliqua. Ut enim ad minim veniam, quis nostrud exercitation ullamco laboris nisi ut aliquip ex ea commodo consequat. Duis aute irure dolor in reprehenderit in voluptate velit esse cillum dolore eu fugiat nulla pariatur. Excepteur sint occaecat cupidatat non proident, sunt in culpa qui officia deserunt mollit anim id est laborum.
  </div>

  <p class="fine-print fine-print--ingredients">Ingredients: water, aloe leaf juice, coconut soap base, glycerin, citrus oil, plant extract. Made in small batches. Net 250 ml.</p>

  <div class="product-art" role="img" aria-label="Aloe vera plant with green water droplets"></div>

  <div class="brand">
    <p class="brand-name">Velbrook</p>
    <p class="brand-name brand-name--second">Naturals</p>
  </div>
  <p class="tagline">Pure Plant Fresh</p>

  <p class="fine-print fine-print--right-top">Refill bottles available in store. Please recycle this pack after use. Keep away from eyes. Store in a cool dry place out of sun.</p>

  <section class="direction">
    <h2 class="direction-title">Direction :</h2>
    <p class="direction-body">Lorem ipsum dolor sit amet consectetur adipiscing elit, sed do eiusmod tempor incididunt ut labore et dolore magna aliqua. Ut enim ad minim veniam, quis nostrud exercitation ullamco laboris nisi ut aliquip ex ea commodo consequat. Duis aute irure dolor in reprehenderit in voluptate velit esse cillum dolore eu fugiat nulla pariatur. Excepteur sint occaecat cupidatat non proident, sunt in culpa qui officia deserunt mollit anim id est laborum.</p>
  </section>
</main>
</body>
</html>
```